New Business Card Design Project

The legal name of the company is TTTolvane, we also refer to it as simply Tolvane or you could also use the initials TTT...... please feel creative.
Excellent design.
On the second side, if you could image North and South America on each drop of water ... it almost looks like that now.
The website is www.tttolvane.com
Attached is another card with the required information; no addresses.

Industry/Entity Type

Legal

```html
<!DOCTYPE html>
<html lang="en">
<head>
<meta charset="utf-8">
<title>Tolvane Business Card</title>
<link rel="stylesheet" href="https://fonts.googleapis.com/css2?family=Montserrat:wght@400;500;700&display=swap">
<style>
  :root {
    --backdrop: #ebe6db;
    --card-white: #f7f7f5;
    --gold-light: #c9b47c;
    --gold: #a48c4c;
    --gold-deep: #8a7437;
    --ink-brown: #3f3214;
    --text-light: #fbf8ee;
  }
  html, body {
    margin: 0;
    width: 1200px;
    height: 891px;
    overflow: hidden;
    background: var(--backdrop);
    font-family: "Montserrat", sans-serif;
  }
  .card {
    position: absolute;
    left: 268px;
    width: 665px;
    height: 380px;
    overflow: hidden;
    box-shadow: 0 8px 24px rgba(60, 48, 20, 0.18);
  }
  .card-front { top: 40px; background: var(--card-white); }
  .card-back  { top: 471px; background: linear-gradient(135deg, var(--gold-light), var(--gold-deep)); }
  .card-shapes { position: absolute; inset: 0; }

  .brand {
    position: absolute;
    left: 30px;
    top: 168px;
    width: 110px;
    display: flex;
    flex-direction: column;
    align-items: center;
    gap: 10px;
  }
  .brand-dot {
    width: 54px;
    height: 54px;
    border-radius: 50%;
    background: radial-gradient(circle at 40% 35%, var(--gold-light), var(--gold));
  }
  .brand-name {
    font-weight: 500;
    font-size: 14px;
    letter-spacing: 3px;
    color: var(--gold);
  }

  .holder {
    position: absolute;
    left: 200px;
    top: 206px;
    color: var(--ink-brown);
  }
  .holder-name {
    margin: 0;
    font-weight: 700;
    font-size: 16px;
    letter-spacing: 0.5px;
  }
  .holder-role {
    margin: 3px 0 0;
    font-weight: 400;
    font-size: 11px;
  }

  .contacts {
    position: absolute;
    left: 486px;
    top: 173px;
    margin: 0;
    padding: 0;
    list-style: none;
    color: var(--text-light);
    font-size: 12px;
  }
  .contacts li {
    display: flex;
    align-items: center;
    gap: 9px;
    height: 26px;
  }
  .contacts svg {
    width: 12px;
    height: 12px;
    fill: none;
    stroke: var(--text-light);
    stroke-width: 2;
  }

  .back-brand {
    position: absolute;
    inset: 0;
    display: flex;
    flex-direction: column;
    align-items: center;
    justify-content: center;
    gap: 14px;
  }
  .back-brand .brand-dot {
    width: 70px;
    height: 70px;
    background: var(--card-white);
  }
  .back-brand .brand-name {
    font-size: 20px;
    letter-spacing: 5px;
    color: var(--text-light);
  }
</style>
</head>
<body>
  <div class="card card-front">
    <svg class="card-shapes" viewBox="0 0 665 380" aria-hidden="true">
      <defs>
        <linearGradient id="goldBand" x1="0" y1="0" x2="1" y2="1">
          <stop offset="0" stop-color="#c9b47c"/>
          <stop offset="1" stop-color="#8f7a3c"/>
        </linearGradient>
      </defs>
      <polygon points="30,28 400,28 392,36 30,36" fill="#8f7a3c"/>
      <polygon points="190,150 420,150 390,300 160,300" fill="url(#goldBand)"/>
      <polygon points="430,150 440,150 410,300 400,300" fill="#a48c4c"/>
      <polygon points="450,150 458,150 428,300 420,300" fill="#a48c4c"/>
      <polygon points="470,150 665,150 665,300 440,300" fill="url(#goldBand)"/>
      <rect x="430" y="342" width="200" height="6" fill="#8f7a3c"/>
    </svg>

    <div class="brand">
      <span class="brand-dot"></span>
      <span class="brand-name">TOLVANE</span>
    </div>

    <div class="holder">
      <p class="holder-name">DANIEL WHITMORE</p>
      <p class="holder-role">Managing Director</p>
    </div>

    <ul class="contacts">
      <li><svg viewBox="0 0 16 16"><rect x="3" y="2" width="10" height="12" rx="1"/></svg>014 820 3517</li>
      <li><svg viewBox="0 0 16 16"><path d="M4 2l3 3-2 2c1 2 2 3 4 4l2-2 3 3-2 2C7 14 2 9 2 4z"/></svg>014 820 3518</li>
      <li><svg viewBox="0 0 16 16"><rect x="2" y="4" width="12" height="9"/><path d="M2 4l6 5 6-5"/></svg>office@tttolvane.com</li>
      <li><svg viewBox="0 0 16 16"><circle cx="8" cy="8" r="6"/><path d="M2 8h12M8 2c3 3 3 9 0 12M8 2c-3 3-3 9 0 12"/></svg>www.tttolvane.com</li>
    </ul>
  </div>

  <div class="card card-back">
    <svg class="card-shapes" viewBox="0 0 665 380" aria-hidden="true">
      <polygon points="40,0 52,0 12,90 0,90" fill="#f7f7f5"/>
      <polygon points="70,0 80,0 40,90 30,90" fill="#f7f7f5"/>
      <polygon points="625,290 635,290 595,380 585,380" fill="#f7f7f5"/>
      <polygon points="653,290 665,290 625,380 613,380" fill="#f7f7f5"/>
    </svg>
    <div class="back-brand">
      <span class="brand-dot"></span>
      <span class="brand-name">TOLVANE</span>
    </div>
  </div>
</body>
</html>
```